New website design for 7vlink

REQUEST FOR PROPOSAL FOR THE DEVELOPMENT 7VLINK WEBSITE

About 7VLINK

7VLINK Nigeria Ltd (7VLINK) is privately owned provider of Information and Communication Technology solutions. The Company has been engaged in Fibre Optic deployments, Wireless Deployments, IP/Data Communication Deployment, Enterprise Network & Infrastructure Solutions and Business Critical infrastructure Management to clients in both private and public sectors. . For more information, please visit www.7vlinkgroup.example .

Project Background.

7VLINK is currently about to roll out her Internet services to both Corporate and Residential market type customers. We need to develop a new site with appeal to the Nigerian market (we must have black people in pictures if we decide to use people but it can also be mixed) but yet have an international appeal. The business has been split into 3 critical service areas:
1. ISP Services
2. Technology Projects
3. Managed Services

The fourth one which more of an activity is 4. Innovation Center

Full Project Scope

Look and feel

We need a website that is CMS (Content Management System) based and that would have WOW! effect on visitor (simple, clean, yet futuristic and techy) , also it is important to try to capture visitors to the website by providing an online chat function. Please visit: http://layoutbazaar.example/item/brightops-premium-responsive-wordpress-theme/full_screen_preview/5820417 (this is almost exactly what we want and can serve as guide for design). You can also visit http://www.7vlinkgroup.example/demowp/ (see a sample of what someone did but we were not too impressed. the site is not neat/crisp. The theme pictures are content should be useful as well).

We have also come across some other inspiration web themes/layout that you may find useful for reference:
1. http://quellstudio.example/wp-content/uploads/2012/03/bxm7.jpg
2. http://www.artpoolhub.example/design/6418093
3. http://taskmeadow.example/index

Please use our 7VLINK logo to guide your color theme for our website

Top Navigation

Again using http://layoutbazaar.example/item/brightops-premium-responsive-wordpress-theme/full_screen_preview/5820417 ( i.e where home , About, gallery, portolio, news, Contacts) as reference we would want the following 3 main navigation buttons only ( Which you will notice is in harmony with our logo “ People , Solutions, Possibilities):
The Top three Navigation Buttons

1. People (Main Menu)
a. About Us
b. Team
c. Customers
d. Partners
e. Investor Relation
f. Contact Us
2. Solutions ( Main Menu)
a. Internet Services (sub menu)
i. Residential Users
ii. Business

b. Technology Projects (sub menu)
i. Vexor Advanced Services
ii. Networks and Infrastructure
iii. Software & Enterprise Apps
iv. Systems Integration

c. Managed Services (sub menu)
i. Managed IT
ii. Sky Haven
iii. Data Center & Co-location
iv. Managed PBX
v. Managed Video Conferencing

3. Possibilities ( Main Menu)
a. 7VLINK Labs
b. Co-innovation
c. Angel investments

The main pictures and Slides
Again using http://layoutbazaar.example/item/brightops-premium-responsive-wordpress-theme/full_screen_preview/5820417 as reference the slide Please refer and replace:
1. “Everything starts with a GREAT SOLUTIONS” please replace with “Access Reliable and High Speed INTERNET SERVICES”
2. “ Innovative ways PERFECT RESULTS” Please replace with “ Reduce IT costs, Focus on your Business - MANAGED SERVICES
3. “A driving force IN YOUR BUSINESS” please replace with “ Leverage on our Pool of Certified specialist for your TECHNOLOGY PROJECTS”
4. “The one and only the best IT COMPANY” please replace with “ We Pioneer and seek to Solve Challenges at our INNOVATION CENTER
Please look for appropriate theme pictures to represent the slides above and also reference http://www.7vlinkgroup.example/demowp/

Industry/Entity Type

Communication

Requirements
Nice to have
• Must haves: content management system in the long run so we can put updates.SEO and very light and fast loading of the webpages.

```html
<!DOCTYPE html>
<html lang="en">
<head>
<meta charset="utf-8">
<title>7vlink — People, Solutions, Possibilities</title>
<link rel="stylesheet" href="https://fonts.googleapis.com/css2?family=Arimo:wght@400;700&family=Oswald:wght@300;400&display=swap">
<style>
:root{
  --page-bg:#e8e8e8;
  --topbar-bg:#dadada;
  --ink:#333333;
  --ink-soft:#666666;
  --ink-faint:#8a8a8a;
  --brand-blue:#2b8fd0;
  --brand-blue-light:#3fb0e8;
  --brand-green:#8cc63f;
  --brand-navy:#2c3a78;
  --arrow-red:#e2623a;
  --btn-dark:#3a3a3a;
  --white:#ffffff;
}
*{box-sizing:border-box;margin:0;padding:0}
html,body{width:1200px;height:895px;overflow:hidden}
body{background:radial-gradient(ellipse at 50% 20%,#f6f6f6 0%,var(--page-bg) 70%);font-family:"Arimo",Arial,sans-serif;color:var(--ink);position:relative}
.abs{position:absolute;white-space:nowrap}

.topbar{left:0;top:0;width:1200px;height:21px;background:var(--topbar-bg)}
.topbar__text{right:333px;top:6px;font-size:8px;color:var(--ink-soft)}
.topbar__call{left:875px;top:3px;font-size:11px;color:#3a4a6a}

.logo{left:222px;top:40px;display:flex;align-items:center;gap:10px}
.logo__dot{width:42px;height:42px;border-radius:50%;background:var(--brand-blue-light)}
.logo__name{font-weight:700;font-size:28px;color:var(--brand-navy);line-height:1}

.search{left:798px;top:62px;width:158px;height:18px;display:flex}
.search__field{width:142px;height:18px;background:var(--white);border:1px solid #e0e0e0}
.search__btn{width:16px;height:18px;background:var(--brand-green)}

.nav{left:217px;top:109px;width:766px;height:40px;background:linear-gradient(#4a4a4a,#262626);border-radius:3px 3px 0 0;display:flex}
.nav__item{height:40px;line-height:36px;font-size:11px;color:var(--white);border-right:1px solid #555;text-align:center}
.nav__item--active{background:linear-gradient(#2f2f2f,#1f1f1f)}

.hero{left:217px;top:149px;width:766px;height:316px;background:linear-gradient(100deg,#2a3344 0%,#4a5870 40%,#8e9bb0 62%,#3a4455 80%,#1e2533 100%)}
.hero__title{left:265px;top:232px;font-family:"Oswald",sans-serif;font-weight:400;font-size:25px;color:var(--white);letter-spacing:-.5px}
.hero__accent{left:290px;top:263px;font-family:"Oswald",sans-serif;font-weight:300;font-size:40px;color:var(--brand-blue-light);letter-spacing:-.5px;line-height:1.1}

.slide-tab{top:382px;width:158px;height:52px;text-align:center;font-family:"Oswald",sans-serif;padding-top:11px;line-height:14px;box-shadow:0 1px 3px rgba(0,0,0,.4)}
.slide-tab__line{font-size:10.5px;color:#333;letter-spacing:-.2px}
.slide-tab__accent{font-size:12px;color:var(--brand-blue);font-weight:300}
.slide-tab--light{background:rgba(240,243,247,.88)}
.slide-tab--current{background:rgba(25,28,34,.9)}
.slide-tab--current .slide-tab__line{color:var(--white)}
.slide-tab--current .slide-tab__accent{color:var(--brand-blue-light)}
.slide-arrow{top:403px;width:11px;height:11px;border-radius:50%;display:flex;align-items:center;justify-content:center}

.dropdown{left:295px;top:149px;width:122px;background:#2a2a2a;border-radius:0 0 3px 3px}
.dropdown__item{height:19px;line-height:19px;padding-left:12px;font-size:7.5px;color:var(--white);border-bottom:1px solid #3c3c3c}
.dropdown__item--current{color:var(--brand-blue-light)}

.content{left:217px;top:465px;width:766px;height:430px;background:#f8f8f8}
.welcome{left:243px;top:486px;font-size:18px;font-weight:400;color:var(--ink)}
.welcome b{color:var(--brand-green)}
.rule{height:1px;background:#cfcfcf}

.service__photo{width:158px;height:120px}
.service__title{font-size:13.5px;color:var(--brand-blue);letter-spacing:.2px}
.service__sub{font-size:10px;color:var(--ink)}
.service__list{list-style:none;width:158px}
.service__list li{height:22px;line-height:22px;font-size:7.5px;color:var(--ink-soft);border-bottom:1px solid #e4e4e4;padding-left:18px;position:relative}
.service__list li::before{content:"→";position:absolute;left:4px;color:var(--arrow-red);font-size:8px}
.btn{height:22px;line-height:22px;padding:0 9px;font-size:8.5px;color:var(--white)}
.btn--dark{background:var(--btn-dark)}
.btn--blue{background:var(--brand-blue-light)}
.section-title{font-size:16px;font-weight:400;color:var(--ink)}

.chat{left:798px;top:522px;width:158px;height:133px;background:linear-gradient(#3fb2ec,#2b97d8)}
.chat__q{left:810px;top:533px;font-size:10px;color:var(--white)}
.chat__big{left:809px;top:549px;font-size:31px;color:var(--white);line-height:1}
.chat__mid{left:810px;top:580px;font-size:15px;color:var(--white)}
.chat__hours{left:812px;top:600px;font-size:8px;color:#d6ecfa}
.chat__btn{left:810px;top:621px;width:63px;height:22px;line-height:22px;text-align:center;font-size:8px;color:var(--white);background:var(--btn-dark)}

.quote{left:798px;top:681px;width:158px;height:80px;background:var(--brand-green)}
.quote__mark{left:810px;top:686px;font-family:Georgia,serif;font-weight:700;font-size:48px;color:var(--white);line-height:1}
.quote__text{left:847px;top:693px;width:104px;white-space:normal;font-family:Georgia,serif;font-style:italic;font-size:9.5px;color:var(--white);line-height:13px}

.feed__title{left:798px;top:784px;font-size:11px;color:var(--ink)}
.feed__arrow{top:785px;width:12px;height:12px;border-radius:50%;display:flex;align-items:center;justify-content:center}
.feed__icon{left:800px;top:829px;width:10px;height:10px;border-radius:50%;background:#9aa0a6}
.feed__text{left:821px;top:828px;width:135px;white-space:normal;font-size:7.8px;color:var(--ink-soft);line-height:11.5px}
.feed__link{background:var(--brand-blue-light);color:var(--white);padding:0 2px}
.feed__time{left:821px;top:882px;font-size:7.8px;color:var(--ink-faint)}
</style>
</head>
<body>
  <div class="abs topbar"></div>
  <div class="abs topbar__text">For Immediate Onsite or Remote Support</div>
  <div class="abs topbar__call">Call: 01-5550142</div>

  <div class="abs logo"><span class="logo__dot"></span><span class="logo__name">7vlink</span></div>

  <div class="abs search"><div class="search__field"></div><div class="search__btn">
    <svg width="16" height="18" viewBox="0 0 16 18"><circle cx="7.5" cy="8.5" r="3" fill="none" stroke="#fff" stroke-width="1.3"/><line x1="9.7" y1="10.7" x2="12" y2="13" stroke="#fff" stroke-width="1.3"/></svg>
  </div></div>

  <nav class="abs nav">
    <div class="nav__item nav__item--active" style="width:77px">People</div>
    <div class="nav__item" style="width:89px">Solutions</div>
    <div class="nav__item" style="width:94px">Possibilities</div>
    <div class="nav__item" style="width:79px">Contact</div>
  </nav>

  <div class="abs hero" role="img" aria-label="Photo of a server room with racks of network equipment"></div>
  <div class="abs hero__title">Access Reliable and High Speed</div>
  <div class="abs hero__accent">INTERNET SERVICES</div>

  <div class="abs slide-arrow" style="left:225px;background:#d8d8d8"><svg width="6" height="6" viewBox="0 0 6 6"><path d="M4 1L2 3l2 2" fill="none" stroke="#333" stroke-width="1"/></svg></div>
  <div class="abs slide-tab slide-tab--current" style="left:244px"><div class="slide-tab__line">Access Reliable and High Speed</div><div class="slide-tab__accent">INTERNET SERVICES</div></div>
  <div class="abs slide-tab slide-tab--light" style="left:429px"><div class="slide-tab__line" style="font-size:9.5px">Reduce IT costs, Focus on your Business</div><div class="slide-tab__accent">MANAGED SERVICES</div></div>
  <div class="abs slide-tab slide-tab--light" style="left:614px"><div class="slide-tab__line">Leverage on our Pool of specialist</div><div class="slide-tab__accent">TECHNOLOGY PROJECTS</div></div>
  <div class="abs slide-tab slide-tab--light" style="left:798px"><div class="slide-tab__line">We Solve Challenges at our</div><div class="slide-tab__accent">INNOVATION CENTER</div></div>
  <div class="abs slide-arrow" style="left:963px;background:#222"><svg width="6" height="6" viewBox="0 0 6 6"><path d="M2 1l2 2-2 2" fill="none" stroke="#fff" stroke-width="1"/></svg></div>

  <div class="abs dropdown">
    <div class="dropdown__item dropdown__item--current">About Us</div>
    <div class="dropdown__item">Team</div>
    <div class="dropdown__item">Customers</div>
    <div class="dropdown__item">Partners</div>
  </div>

  <main class="abs content"></main>
  <h1 class="abs welcome">Welcome to <b>7V networks!</b></h1>
  <div class="abs rule" style="left:243px;top:521px;width:527px"></div>

  <div class="abs service__photo" style="left:243px;top:541px;background:linear-gradient(#e9e9e9,#9a8f86 55%,#f8f8f8)" role="img" aria-label="Photo of business people in suits in an office"></div>
  <div class="abs service__title" style="left:243px;top:681px">INNOVATION CENTRE</div>
  <div class="abs service__sub" style="left:243px;top:699px">Services</div>
  <ul class="abs service__list" style="left:243px;top:718px">
    <li>Consectetur adipisicing elit</li><li>Sed do eiusmod tempor incid</li><li>Idunt ut labore et dolore</li><li>Magna aliqua enim</li>
  </ul>
  <div class="abs btn btn--dark" style="left:244px;top:817px">Click to Call Now!</div>

  <div class="abs service__photo" style="left:427px;top:541px;background:linear-gradient(#f8f8f8,#c9c4c0 50%,#f8f8f8)" role="img" aria-label="Photo of two colleagues working together at a laptop"></div>
  <div class="abs service__title" style="left:427px;top:681px">MANAGED SERVICES</div>
  <div class="abs service__sub" style="left:427px;top:699px">Research</div>
  <ul class="abs service__list" style="left:427px;top:718px">
    <li>Minim veniam quis nostrud</li><li>Exercitation ullamco laboris nisi</li><li>Ut aliquip ex ea commodo</li><li>Consequat  duis aute irure</li>
  </ul>
  <div class="abs btn btn--blue" style="left:428px;top:817px">Click to Call Now!</div>

  <div class="abs service__photo" style="left:612px;top:541px;background:linear-gradient(#2a3446,#4d5a70 60%,#f8f8f8)" role="img" aria-label="Photo of network switches in a server rack"></div>
  <div class="abs service__title" style="left:612px;top:681px">TECHNOLOGY PROJECTS</div>
  <div class="abs service__sub" style="left:612px;top:699px">and Efficiency</div>
  <ul class="abs service__list" style="left:612px;top:718px">
    <li>Magna aliqua enim</li><li>Consectetur adipisicing elit</li><li>Sed do eiusmod tempor incid</li><li>Idunt ut labore et dolore</li>
  </ul>
  <div class="abs btn btn--blue" style="left:613px;top:817px">Click to Call Now!</div>

  <h2 class="abs section-title" style="left:242px;top:861px">How it works?</h2>
  <h2 class="abs section-title" style="left:427px;top:861px">Why choose us?</h2>
  <h2 class="abs section-title" style="left:611px;top:861px">Perfect results</h2>
  <div class="abs rule" style="left:243px;top:893px;width:158px"></div>
  <div class="abs rule" style="left:427px;top:893px;width:158px"></div>
  <div class="abs rule" style="left:612px;top:893px;width:158px"></div>

  <aside>
    <div class="abs chat"></div>
    <div class="abs chat__q">Questions!</div>
    <div class="abs chat__big">Chat</div>
    <div class="abs chat__mid">With us live!</div>
    <div class="abs chat__hours">Mon- Fri 8am-9pm</div>
    <div class="abs chat__btn">Click Here!</div>

    <div class="abs quote"></div>
    <div class="abs quote__mark">“</div>
    <div class="abs quote__text">Lorem ipsum dolor sit amet, consectetur ad-ipisicing elit, sed do eiusmod tempor.</div>

    <div class="abs feed__title">Chirper Feed</div>
    <div class="abs feed__arrow" style="left:928px;background:#d0d0d0"><svg width="6" height="6" viewBox="0 0 6 6"><path d="M4 1L2 3l2 2" fill="none" stroke="#fff" stroke-width="1"/></svg></div>
    <div class="abs feed__arrow" style="left:944px;background:#222"><svg width="6" height="6" viewBox="0 0 6 6"><path d="M2 1l2 2-2 2" fill="none" stroke="#fff" stroke-width="1"/></svg></div>
    <div class="abs rule" style="left:798px;top:812px;width:158px"></div>
    <div class="abs feed__icon"></div>
    <p class="abs feed__text">Lorem ipsum dolor sit amet conse ctetur adipisicing elit, sed incididunt ut labore et dolore magna aliqua. <span class="feed__link">http://sh.example/k4Tq</span></p>
    <div class="abs feed__time">(about 6 hours ago)</div>
  </aside>
</body>
</html>
```